Create a business Card for a Women Owned Business Body Positive Company. The winner we hope to work with on other projects coming up for grand opening for flyers, postcards, email marketing, facebook page, stationary, labels, tshirt design....
We would like if possible in the background of the card a infinity symbol or crown if it fits into the design if not it's ok. But I am open to all suggestions we had alot problems with the our new logo being created this time sad to say :(

Our colors are Royal Purple, Grey, Black Thank you in advance for your talent, you hard work and your submissions!
Delia and Nadine :)
Updates

my Logo is velvet harbor boutique which is purple and has a heart and infinity sign in it and my colors are purple silver and black only of another card i had done nothing else. My logo is VELVET HARBOR BOUTIQUE LOGO

Industry/Entity Type

Retail

Contact Information for Business Card

website: www.velvtharborboutiques.example email: sales@velvetharborboutique.example
Delia Pruett & Nadine Kolb Owners

Font styles to use
Script

Colors
b768aa

Requirements
Must have
• COLORS ARE PURPLE BLACK AND GREY
Nice to have
• INFINITY SIGNING IN THE BACKGROUND

```html
<!DOCTYPE html>
<html lang="en">
<head>
<meta charset="utf-8">
<title>Velvet Harbor Boutique – Business Card</title>
<link rel="stylesheet" href="https://fonts.googleapis.com/css2?family=Lato:wght@400;700&display=swap">
<style>
  :root {
    --royal-purple: #7b4192;
    --ink: #1a1a1a;
    --paper: #ffffff;
    --stage: #3b3b3b;
    --grey: #6d6d6d;
  }
  * { box-sizing: border-box; margin: 0; padding: 0; }
  html, body { width: 1200px; height: 900px; overflow: hidden; }
  body {
    background: var(--stage);
    font-family: "Lato", Arial, sans-serif;
    position: relative;
  }
  .card {
    position: absolute;
    left: 290px;
    width: 620px;
    height: 354px;
    overflow: hidden;
  }
  .card-back { top: 68px; background: var(--royal-purple); color: var(--paper); }
  .card-front { top: 478px; background: var(--paper); color: var(--ink); }

  /* back */
  .back-brand {
    position: absolute; left: 60px; right: 60px; top: 124px;
    display: flex; align-items: center; justify-content: center; gap: 12px;
  }
  .brand-dot { width: 12px; height: 12px; border-radius: 50%; background: currentColor; flex: none; }
  .brand-name {
    font-weight: 700; letter-spacing: 0.06em; line-height: 1.15;
  }
  .back-brand .brand-name { font-size: 30px; color: var(--paper); white-space: nowrap; }
  .back-web {
    position: absolute; left: 0; right: 0; top: 236px;
    text-align: center; font-size: 17px; letter-spacing: 0.03em;
  }

  /* front */
  .front-wave { position: absolute; inset: 0; }
  .front-brand {
    position: absolute; left: 34px; top: 34px;
    display: flex; align-items: center; gap: 10px;
    color: var(--royal-purple);
  }
  .front-brand .brand-name { font-size: 25px; color: var(--royal-purple); }
  .front-brand .brand-dot { width: 10px; height: 10px; }
  .owners { position: absolute; left: 34px; top: 112px; }
  .owner-names {
    color: var(--royal-purple); font-weight: 700; font-size: 19px; line-height: 1.15;
  }
  .owner-role { font-size: 14px; margin-top: 3px; }
  .address { position: absolute; left: 34px; top: 196px; font-size: 14px; line-height: 1.35; }
  .contact-list {
    position: absolute; left: 210px; top: 238px; list-style: none;
    font-size: 14px; line-height: 1.5;
  }
  .contact-list li { display: flex; align-items: center; gap: 8px; white-space: nowrap; }
  .contact-icon { width: 12px; height: 12px; fill: var(--royal-purple); flex: none; }
</style>
</head>
<body>

<section class="card card-back" aria-label="Business card back">
  <div class="back-brand">
    <span class="brand-dot"></span>
    <span class="brand-name">VELVET HARBOR BOUTIQUE</span>
  </div>
  <p class="back-web">www.velvtharborboutiques.example</p>
</section>

<section class="card card-front" aria-label="Business card front">
  <svg class="front-wave" viewBox="0 0 620 354" width="620" height="354" aria-hidden="true">
    <path d="M306 0 C440 60 500 200 478 354 L620 354 L620 0 Z" fill="#1a1a1a"/>
    <path d="M320 0 C456 60 522 200 502 354 L620 354 L620 0 Z" fill="#ffffff"/>
    <path d="M328 0 C466 60 532 200 512 354 L620 354 L620 0 Z" fill="#7b4192"/>
  </svg>

  <div class="front-brand">
    <span class="brand-dot"></span>
    <span class="brand-name">VELVET HARBOR<br>BOUTIQUE</span>
  </div>

  <div class="owners">
    <p class="owner-names">Delia Pruett &amp;<br>Nadine Kolb</p>
    <p class="owner-role">Owners</p>
  </div>

  <p class="address">418 Marlow Court<br>Fairbrook, TX 77512</p>

  <ul class="contact-list">
    <li>
      <svg class="contact-icon" viewBox="0 0 24 24"><path d="M6.6 10.8a15 15 0 0 0 6.6 6.6l2.2-2.2c.3-.3.7-.4 1-.2 1.1.4 2.3.6 3.6.6.6 0 1 .4 1 1V20c0 .6-.4 1-1 1A17 17 0 0 1 3 4c0-.6.4-1 1-1h3.5c.6 0 1 .4 1 1 0 1.3.2 2.5.6 3.6.1.3 0 .7-.2 1z"/></svg>
      555 014 2290
    </li>
    <li>
      <svg class="contact-icon" viewBox="0 0 24 24"><path d="M7 1h10a2 2 0 0 1 2 2v18a2 2 0 0 1-2 2H7a2 2 0 0 1-2-2V3a2 2 0 0 1 2-2zm0 3v14h10V4zm5 15.5a1.2 1.2 0 1 0 0 2.4 1.2 1.2 0 0 0 0-2.4z"/></svg>
      555 014 2291
    </li>
    <li>
      <svg class="contact-icon" viewBox="0 0 24 24"><path d="M2 5h20v14H2zm2 2v.5l8 5 8-5V7l-8 5z"/></svg>
      sales@velvetharborboutique.example
    </li>
    <li>
      <svg class="contact-icon" viewBox="0 0 24 24"><path d="M12 2a10 10 0 1 0 0 20 10 10 0 0 0 0-20zm6.9 9h-3a15 15 0 0 0-1.2-5.6A8 8 0 0 1 18.9 11zM12 4c.9 1.2 1.8 3.6 1.9 7h-3.8c.1-3.4 1-5.8 1.9-7zM9.3 5.4A15 15 0 0 0 8.1 11h-3a8 8 0 0 1 4.2-5.6zM5.1 13h3a15 15 0 0 0 1.2 5.6A8 8 0 0 1 5.1 13zm6.9 7c-.9-1.2-1.8-3.6-1.9-7h3.8c-.1 3.4-1 5.8-1.9 7zm2.7-1.4a15 15 0 0 0 1.2-5.6h3a8 8 0 0 1-4.2 5.6z"/></svg>
      www.velvtharborboutiques.example
    </li>
  </ul>
</section>

</body>
</html>
```